Real Estate Agent who sells beach front condos needs a template for a monthly postcard campaign.

Carla Jenrick, Homebroker with Quintavo Real Estate and Development, Licensed in Florida and Alabama, 251-468-3072, carlajenrick.example, carlamjenrick@mailbox.example. Need a postcard template which will allow me to type in recipe instructions and insert a photo of the finished food product. The recipe and photo will change every month, so I need this to be something I can easily change and reorder every month. I sell beach condos primarily. I'd like large photos of the food. Glossy card on both sides.

Target Market(s)

buyers and sellers of homes, condos, lots

Industry/Entity Type

Real Estate Agent

Requirements
Must have
• my contact information, my photo, my company name (Quintavo Real Estate and Development), the Equal Dwelling Logo, the Homebroker Logo, the statement "Contact me for all your Real Estate needs!", a template on the front side that will let me change the photograph at will, and a template on the back side that will let me type words.
Nice to have
• For my contact info and photo to stand out also.

```html
<!DOCTYPE html>
<html lang="en">
<head>
<meta charset="utf-8">
<title>Carla Jenrick – Monthly Recipe Postcard</title>
<link rel="stylesheet" href="https://fonts.googleapis.com/css2?family=Dancing+Script:wght@700&family=Pacifico&family=Roboto+Condensed:wght@700&family=Roboto:wght@400;700&family=Open+Sans:wght@400&display=swap">
<style>
  :root {
    --stage: #2b2b2b;
    --sky: #1b9fd8;
    --lime: #d9e81c;
    --navy: #153a66;
    --cream: #f5f1e6;
    --white: #ffffff;
    --photo-dark: #5a3320;
    --photo-mid: #8a5a3c;
    --photo-light: #e9e2d6;
  }
  * { margin: 0; padding: 0; box-sizing: border-box; }
  html, body { width: 900px; height: 1200px; overflow: hidden; }
  body { background: var(--stage); position: relative; font-family: "Roboto", Arial, sans-serif; }

  .postcard { position: absolute; left: 95px; width: 720px; overflow: hidden; }
  .postcard-front { top: 55px; height: 517px; }
  .postcard-back { top: 625px; height: 515px; background: var(--white); }
  .postcard svg.card-shapes { position: absolute; inset: 0; }

  .agent-name { position: absolute; left: 32px; top: 48px; font-family: "Dancing Script", cursive; font-size: 46px; color: var(--white); line-height: 1; }
  .agent-tagline { position: absolute; left: 34px; top: 98px; font-family: "Dancing Script", cursive; font-size: 22px; color: var(--white); line-height: 1; }
  .agent-license { position: absolute; left: 46px; top: 140px; font-family: "Open Sans", sans-serif; font-size: 15px; color: var(--white); }
  .front-contact { position: absolute; left: 42px; top: 216px; font-family: "Roboto Condensed", sans-serif; font-weight: 700; font-size: 54px; color: var(--sky); line-height: 1; }
  .front-pitch { position: absolute; left: 46px; top: 280px; width: 260px; font-family: "Pacifico", cursive; font-size: 21px; color: var(--navy); line-height: 1.3; }
  .front-website { position: absolute; left: 40px; top: 460px; font-family: "Roboto", sans-serif; font-weight: 700; font-size: 26px; color: var(--white); }

  .partner-row { position: absolute; left: 520px; top: 462px; display: flex; align-items: center; gap: 10px; }
  .company-name { font-family: "Roboto", sans-serif; font-size: 12px; font-weight: 700; color: var(--photo-mid); display: flex; align-items: center; gap: 4px; }
  .company-name .mark { width: 10px; height: 10px; background: var(--photo-mid); }
  .badge-square { width: 14px; height: 14px; background: #333; }
  .badge-rect { width: 48px; height: 16px; border: 2px solid #333; }

  .recipe-title { position: absolute; left: 50px; top: 38px; font-family: "Pacifico", cursive; font-size: 34px; color: var(--white); line-height: 1; }
  .section-heading { position: absolute; font-family: "Roboto", sans-serif; font-weight: 700; font-size: 15px; color: var(--navy); }
  .ingredients-heading { left: 26px; top: 108px; }
  .procedure-heading { left: 29px; top: 214px; }
  .ingredient-list { position: absolute; top: 140px; list-style: none; font-size: 12px; color: var(--navy); line-height: 15.5px; }
  .ingredient-list li::before { content: ""; display: inline-block; width: 7px; height: 7px; border-radius: 50%; background: var(--sky); margin-right: 8px; vertical-align: 1px; }
  .ingredient-list.col-a { left: 26px; }
  .ingredient-list.col-b { left: 166px; }
  .procedure-text { position: absolute; left: 29px; top: 239px; width: 236px; font-size: 11px; line-height: 14.5px; color: var(--navy); text-align: justify; }

  .agent-photo { position: absolute; left: 29px; top: 333px; width: 92px; height: 105px; background: linear-gradient(160deg, #c9b59a, #6d6058 70%, #3d3a3a); }
  .back-contact { position: absolute; left: 137px; top: 382px; font-family: "Roboto Condensed", sans-serif; font-weight: 700; font-size: 31px; color: var(--sky); line-height: 1; }
  .back-phone { position: absolute; left: 136px; top: 428px; font-family: "Roboto", sans-serif; font-weight: 700; font-size: 19px; color: var(--white); }
  .back-email { position: absolute; left: 33px; top: 471px; font-family: "Roboto", sans-serif; font-weight: 700; font-size: 17px; color: var(--navy); }
</style>
</head>
<body>

<section class="postcard postcard-front">
  <svg class="card-shapes" width="720" height="517" viewBox="0 0 720 517">
    <defs>
      <linearGradient id="food-tones" x1="0" y1="0" x2="1" y2="1">
        <stop offset="0" stop-color="var(--photo-mid)"/>
        <stop offset="0.55" stop-color="var(--photo-dark)"/>
        <stop offset="1" stop-color="var(--photo-light)"/>
      </linearGradient>
    </defs>
    <rect width="720" height="517" fill="var(--sky)"/>
    <rect y="208" width="400" height="157" fill="var(--lime)"/>
    <path d="M400 0 C368 120 372 300 482 517 L720 517 L720 0 Z" fill="var(--lime)"/>
    <path role="img" aria-label="Large photo of this month's finished recipe dish" d="M414 0 C384 120 388 300 496 517 L720 517 L720 0 Z" fill="url(#food-tones)"/>
    <path d="M438 410 C455 450 475 485 496 517 L720 517 L720 410 Z" fill="var(--cream)"/>
  </svg>
  <div class="agent-name">Carla Jenrick</div>
  <div class="agent-tagline">Your Gulf Coast Homebroker</div>
  <div class="agent-license">Licensed in Alabama &amp; Florida</div>
  <div class="front-contact">CONTACT</div>
  <div class="front-pitch">for all your Real Estate needs!</div>
  <div class="front-website">www.carlajenrick.example</div>
  <div class="partner-row">
    <span class="company-name"><span class="mark"></span>QUINTAVO</span>
    <span class="badge-square" role="img" aria-label="Equal Dwelling Logo"></span>
    <span class="badge-rect" role="img" aria-label="Homebroker Logo"></span>
  </div>
</section>

<section class="postcard postcard-back">
  <svg class="card-shapes" width="720" height="515" viewBox="0 0 720 515">
    <defs>
      <clipPath id="panel-clip">
        <path d="M0 0 L375 0 C430 120 432 330 245 515 L0 515 Z"/>
      </clipPath>
    </defs>
    <path d="M0 0 L383 0 C440 120 442 330 255 515 L0 515 Z" fill="var(--lime)"/>
    <g clip-path="url(#panel-clip)">
      <rect width="720" height="515" fill="var(--lime)"/>
      <rect width="720" height="97" fill="var(--sky)"/>
      <rect y="419" width="312" height="42" fill="var(--sky)"/>
    </g>
  </svg>
  <div class="recipe-title">Recipe</div>
  <div class="section-heading ingredients-heading">Ingredients</div>
  <ul class="ingredient-list col-a">
    <li>Lorem ipsum</li><li>dolor sit amet</li><li>consectetur</li><li>adipiscing elit.</li>
  </ul>
  <ul class="ingredient-list col-b">
    <li>Lorem ipsum</li><li>dolor sit amet</li><li>consectetur</li><li>adipiscing elit.</li>
  </ul>
  <div class="section-heading procedure-heading">Procedure</div>
  <p class="procedure-text">Lorem Ipsum is simply dummy text of the printing and typesetting industry. Lorem Ipsum has been the industry's standard dummy text ever since the 1500s, when an unknown printer took a galley of type and scrambled it to make a type specimen book.</p>
  <div class="agent-photo" role="img" aria-label="Portrait photo of Carla Jenrick"></div>
  <div class="back-contact">CONTACT</div>
  <div class="back-phone">251-468-3072</div>
  <div class="back-email">carlamjenrick@mailbox.example</div>
</section>

</body>
</html>
```